Video Learning Web Application Site Design

We are a new company that produce and distribute educational videos using a subscription model on our website. The videos are streamed on our website and users can tailor their own course packages by creating playlists. Each video-lesson are also split into several smaller segments, and it should be easy to find and play those segments.

Please note that both the screenshots and wireframes provided are only how it looks right now, if you as the designer have a better idea on how to present it then please share it.
Updates

Please view the screenshots as well, I believe I forgot to include two buttons on the wireframes that should be on the Our Courses page. Also, there is no need to make a carbon copy of the wireframes/screenshots, I'd like you designers to come up with a better way of displaying the information if possible. For inspiration you can look at sites like ClipNest (I like the simplicity of their design) and to some extent the Prism UI where they divide different areas of the page into clear "zones".

Thanks,

Reason: I have to extend the deadline because I've been really ill the last week. Will go through the current submissions now and provide feedback and looking forward to more submissions.

Target Market(s)

College and University students. Professionals wanting to expand their knowledge and people that want to learn new skills to get a promotion/new job.

Industry/Entity Type

Tailor

Requirements
Must have
• Must include the logo from the file "brightleaf-logo".
• Should include two pages, one of the video-player page and one of the course list.
• Try to incorporate the colors from the logo.
• Please note: If you look at the video-player.png file just below "Starte Tavla, bruke..." there are two rows, those are sub-parts of the lesson. Both these and the main lesson itself must have some easy way to Play and Add to Playlist.
Nice to have
• We prefer flat design, with simple and clean icons. Don't overdo the colors, stay within 3-4 colors with variations of them.
Should not have
• 3D-like elements, lot of shadows or hard to ready text.

```html
<!DOCTYPE html>
<html lang="en">
<head>
<meta charset="utf-8">
<title>brightleaf – Your Courses</title>
<link href="https://fonts.googleapis.com/css2?family=Source+Sans+3:wght@300;400;600;700&display=swap" rel="stylesheet">
<style>
:root{
  --blue:#0a9fcb;
  --blue-dark:#066a95;
  --blue-mid:#0785ad;
  --navy:#083f55;
  --orange:#ef8c25;
  --orange-dark:#de7c1a;
  --text:#4a4a4a;
  --muted:#777;
  --line:#dcdcdc;
  --row:#f2f2f2;
  --page:#ffffff;
  --footer:#ececec;
}
*{box-sizing:border-box;margin:0;padding:0}
html,body{width:1200px;height:1052px;overflow:hidden;background:var(--page)}
body{font-family:"Source Sans 3",Arial,sans-serif;color:var(--text)}
.page{position:relative;width:1168px;height:1024px;transform:scale(1.0274);transform-origin:0 0}
.abs{position:absolute}

/* header */
.site-header{position:absolute;left:0;top:0;width:1168px;height:110px;background:linear-gradient(#fbfbfb,#f1f1f1);border-bottom:1px solid #d6d6d6}
.brand{position:absolute;left:78px;top:24px;display:flex;align-items:center;gap:12px}
.brand-mark{width:62px;height:62px;border-radius:50%;background:var(--blue)}
.brand-name{font-size:50px;font-weight:700;color:#17708f;letter-spacing:0.5px;line-height:1}
.search{position:absolute;left:432px;top:45px;width:312px;height:32px;border:1px solid #c8c8c8;border-radius:16px;background:#fff;padding-left:17px;font-size:14px;font-style:italic;color:#999;line-height:30px}
.search svg{position:absolute;right:11px;top:6px}
.user{position:absolute;left:791px;top:51px;font-size:14px;color:#333}
.btn-logout{position:absolute;left:1000px;top:41px;width:90px;height:35px;border-radius:3px;background:linear-gradient(#f6992d,#e9791a);border:1px solid #d9721a;color:#fff;font-size:16px;text-align:center;line-height:33px}

/* sidebar */
.sidebar{position:absolute;left:72px;top:110px;width:222px;height:859px;background:linear-gradient(var(--blue),var(--blue-dark))}
.nav-group{position:absolute;left:0;width:222px;padding-left:34px;color:#fff;border-bottom:1px solid rgba(255,255,255,.18)}
.nav-group h3{font-size:18px;font-weight:700;letter-spacing:.3px;line-height:22px}
.nav-group a{display:block;font-size:14px;font-weight:300;line-height:20px;color:#eaf7fc;text-decoration:none}
.nav-group.active{background:var(--blue-mid);box-shadow:inset 0 0 0 1px rgba(0,0,0,.12)}
.add-playlist{position:absolute;left:188px;top:18px;width:20px;height:20px;border-radius:50%;background:#083245}

/* main */
.section-title{position:absolute;left:325px;top:127px;font-size:23px;font-weight:300;color:#4d4d4d}
.video{position:absolute;left:326px;top:166px;width:369px;height:222px;background:linear-gradient(#c9c6bd,#8a8780)}
.play{position:absolute;left:162px;top:87px;width:46px;height:46px;border-radius:50%;background:#222;border:2px solid #fff}
.cue-panel{position:absolute;left:722px;top:166px;width:372px;height:222px;background:var(--orange);border-radius:3px;color:#fff}
.cue-panel-head{height:40px;background:var(--orange-dark);border-radius:3px 3px 0 0;padding-left:23px;font-size:19px;line-height:42px}
.cue-label{position:absolute;left:23px;top:51px;font-size:15px}
.cue-list{position:absolute;left:23px;top:78px;width:170px;height:114px;background:#fff;border-radius:2px;padding-top:8px;list-style:none}
.cue-list li{height:22px;line-height:22px;padding-left:15px;font-size:12px;color:#888}
.cue-list li.selected{background:#efefef}
.files{position:absolute;left:209px;top:49px}
.files h4{font-size:15px;font-weight:600;margin-bottom:4px}
.files a{display:block;font-size:13px;font-weight:600;color:#fff;text-decoration:none;line-height:25px}
.files a::before{content:"";display:inline-block;border-left:4px solid #fff;border-top:3px solid transparent;border-bottom:3px solid transparent;margin-right:5px;vertical-align:1px}

.course-title{position:absolute;left:325px;top:414px;font-size:19px;font-weight:300;color:#4a4a4a}
.btn-remove{position:absolute;left:508px;top:412px;width:131px;height:31px;border-radius:3px;background:linear-gradient(#0d4e69,var(--navy));color:#fff;font-size:13px;text-align:center;line-height:31px}
.divider{position:absolute;left:325px;top:453px;width:768px;border-top:1px solid var(--line)}
.btn-cues{position:absolute;left:325px;top:464px;width:121px;height:31px;border-radius:3px;background:linear-gradient(#17b1dd,#0a8fbc);border:1px solid #0a86b0;color:#fff;font-size:13px;text-align:center;line-height:29px}

.cue-tree{position:absolute;left:327px;top:510px;width:763px;height:459px;background:#fff;box-shadow:0 0 5px rgba(0,0,0,.18)}
.tree-item{position:absolute;left:0;width:763px;height:34px;background:var(--row);font-size:15px;color:#444;line-height:34px}
.tree-child{position:absolute;font-size:14px;color:#555;line-height:20px}
.tree-item svg,.tree-child svg{position:absolute}

/* footer */
.site-footer{position:absolute;left:0;top:969px;width:1168px;height:55px;background:var(--footer);border-top:1px solid #dadada}
.social{position:absolute;top:15px;width:23px;height:23px;border-radius:2px}
.copyright{position:absolute;left:857px;top:20px;font-size:12px;color:#666}
</style>
</head>
<body>
<div class="page">

  <header class="site-header">
    <div class="brand"><span class="brand-mark"></span><span class="brand-name">brightleaf</span></div>
    <div class="search">Search here
      <svg width="20" height="20" viewBox="0 0 20 20"><circle cx="11" cy="8" r="6" fill="none" stroke="#aaa" stroke-width="1.6"/><line x1="6.5" y1="12.5" x2="2" y2="17" stroke="#aaa" stroke-width="1.8"/></svg>
    </div>
    <div class="user">Logged in as alex@example.org</div>
    <div class="btn-logout">Log Out</div>
  </header>

  <nav class="sidebar">
    <div class="nav-group" style="top:0;height:78px;padding-top:23px">
      <h3>INTRODUCTION</h3><a>Introduction</a>
    </div>
    <div class="nav-group active" style="top:78px;height:85px;padding-top:13px">
      <h3>MODULES</h3><a>Our Courses</a><a>Your Courese</a>
    </div>
    <div class="nav-group" style="top:163px;height:94px;padding-top:17px">
      <h3>PLAYLISTS</h3><a>My Playlist</a><a>My Playlist 2</a>
      <span class="add-playlist"><svg width="20" height="20" viewBox="0 0 20 20"><path d="M10 5v10M5 10h10" stroke="#fff" stroke-width="2"/></svg></span>
    </div>
  </nav>

  <main>
    <h1 class="section-title">YOUR COURSES</h1>
    <div class="video" role="img" aria-label="Lesson video still: two students working at a laptop">
      <span class="play"><svg width="42" height="42" viewBox="0 0 42 42"><path d="M16 12l13 9-13 9z" fill="#fff"/></svg></span>
    </div>

    <section class="cue-panel">
      <div class="cue-panel-head">Item 1</div>
      <div class="cue-label">cues</div>
      <ul class="cue-list">
        <li>Child 1</li><li class="selected">Child 2</li><li>Child 3</li><li>Child 4</li>
      </ul>
      <div class="files">
        <h4>Files</h4>
        <a>Download Lesseon file</a>
        <a>Download study material</a>
      </div>
    </section>

    <h2 class="course-title">Tavla 2013 - Beginner</h2>
    <div class="btn-remove">Remove this coures</div>
    <div class="divider"></div>
    <div class="btn-cues">Show All Cues</div>

    <section class="cue-tree">
      <!-- group 1 -->
      <div class="tree-item" style="top:3px">
        <svg style="left:24px;top:11px" width="6" height="12" viewBox="0 0 6 12"><path d="M1 1l4 5-4 5" fill="none" stroke="#bbb" stroke-width="1.5"/></svg>
        <svg style="left:36px;top:10px" width="13" height="13" viewBox="0 0 24 24"><path d="M12 2l3 7 7 .6-5.4 4.7 1.7 7.2L12 17.6 5.7 21.5l1.7-7.2L2 9.6 9 9z" fill="var(--orange)"/></svg>
        <svg style="left:53px;top:15px" width="10" height="6" viewBox="0 0 10 6"><path d="M0 0h10L5 6z" fill="#bbb"/></svg>
        <span style="position:absolute;left:69px">Item 1</span>
      </div>
      <div class="tree-child" style="left:56px;top:45px"><svg style="left:0;top:5px" width="6" height="12" viewBox="0 0 6 12"><path d="M1 1l4 5-4 5" fill="none" stroke="#bbb" stroke-width="1.5"/></svg><svg style="left:12px;top:3px" width="13" height="13" viewBox="0 0 24 24"><path d="M12 2l3 7 7 .6-5.4 4.7 1.7 7.2L12 17.6 5.7 21.5l1.7-7.2L2 9.6 9 9z" fill="var(--orange)"/></svg><span style="margin-left:29px">Child 1</span></div>
      <div class="tree-child" style="left:56px;top:70px"><svg style="left:0;top:5px" width="6" height="12" viewBox="0 0 6 12"><path d="M1 1l4 5-4 5" fill="none" stroke="#bbb" stroke-width="1.5"/></svg><svg style="left:12px;top:3px" width="13" height="13" viewBox="0 0 24 24"><path d="M12 2l3 7 7 .6-5.4 4.7 1.7 7.2L12 17.6 5.7 21.5l1.7-7.2L2 9.6 9 9z" fill="var(--orange)"/></svg><span style="margin-left:29px">Child 2</span></div>
      <div class="tree-child" style="left:56px;top:95px"><svg style="left:0;top:5px" width="6" height="12" viewBox="0 0 6 12"><path d="M1 1l4 5-4 5" fill="none" stroke="#bbb" stroke-width="1.5"/></svg><svg style="left:12px;top:3px" width="13" height="13" viewBox="0 0 24 24"><path d="M12 2l3 7 7 .6-5.4 4.7 1.7 7.2L12 17.6 5.7 21.5l1.7-7.2L2 9.6 9 9z" fill="var(--orange)"/></svg><span style="margin-left:29px">Child 3</span></div>

      <!-- group 2 -->
      <div class="tree-item" style="top:139px">
        <svg style="left:24px;top:11px" width="6" height="12" viewBox="0 0 6 12"><path d="M1 1l4 5-4 5" fill="none" stroke="#bbb" stroke-width="1.5"/></svg>
        <svg style="left:36px;top:10px" width="13" height="13" viewBox="0 0 24 24"><path d="M12 2l3 7 7 .6-5.4 4.7 1.7 7.2L12 17.6 5.7 21.5l1.7-7.2L2 9.6 9 9z" fill="var(--orange)"/></svg>
        <svg style="left:53px;top:15px" width="10" height="6" viewBox="0 0 10 6"><path d="M0 0h10L5 6z" fill="#bbb"/></svg>
        <span style="position:absolute;left:69px">Item 2</span>
      </div>
      <div class="tree-child" style="left:56px;top:181px"><svg style="left:0;top:5px" width="6" height="12" viewBox="0 0 6 12"><path d="M1 1l4 5-4 5" fill="none" stroke="#bbb" stroke-width="1.5"/></svg><svg style="left:12px;top:3px" width="13" height="13" viewBox="0 0 24 24"><path d="M12 2l3 7 7 .6-5.4 4.7 1.7 7.2L12 17.6 5.7 21.5l1.7-7.2L2 9.6 9 9z" fill="var(--orange)"/></svg><span style="margin-left:29px">Child 4</span></div>
      <div class="tree-child" style="left:56px;top:206px"><svg style="left:0;top:5px" width="6" height="12" viewBox="0 0 6 12"><path d="M1 1l4 5-4 5" fill="none" stroke="#bbb" stroke-width="1.5"/></svg><svg style="left:12px;top:3px" width="13" height="13" viewBox="0 0 24 24"><path d="M12 2l3 7 7 .6-5.4 4.7 1.7 7.2L12 17.6 5.7 21.5l1.7-7.2L2 9.6 9 9z" fill="var(--orange)"/></svg><span style="margin-left:29px">Child 5</span></div>
      <div class="tree-child" style="left:56px;top:231px"><svg style="left:0;top:5px" width="6" height="12" viewBox="0 0 6 12"><path d="M1 1l4 5-4 5" fill="none" stroke="#bbb" stroke-width="1.5"/></svg><svg style="left:12px;top:3px" width="13" height="13" viewBox="0 0 24 24"><path d="M12 2l3 7 7 .6-5.4 4.7 1.7 7.2L12 17.6 5.7 21.5l1.7-7.2L2 9.6 9 9z" fill="var(--orange)"/></svg><span style="margin-left:29px">Child 6</span></div>

      <!-- group 3 -->
      <div class="tree-item" style="top:285px">
        <svg style="left:16px;top:11px" width="6" height="12" viewBox="0 0 6 12"><path d="M1 1l4 5-4 5" fill="none" stroke="#bbb" stroke-width="1.5"/></svg>
        <svg style="left:28px;top:10px" width="13" height="13" viewBox="0 0 24 24"><path d="M12 2l3 7 7 .6-5.4 4.7 1.7 7.2L12 17.6 5.7 21.5l1.7-7.2L2 9.6 9 9z" fill="var(--orange)"/></svg>
        <svg style="left:45px;top:15px" width="10" height="6" viewBox="0 0 10 6"><path d="M0 0h10L5 6z" fill="#bbb"/></svg>
        <span style="position:absolute;left:61px">Item 2</span>
      </div>
      <div class="tree-child" style="left:48px;top:327px"><svg style="left:0;top:5px" width="6" height="12" viewBox="0 0 6 12"><path d="M1 1l4 5-4 5" fill="none" stroke="#bbb" stroke-width="1.5"/></svg><svg style="left:12px;top:3px" width="13" height="13" viewBox="0 0 24 24"><path d="M12 2l3 7 7 .6-5.4 4.7 1.7 7.2L12 17.6 5.7 21.5l1.7-7.2L2 9.6 9 9z" fill="var(--orange)"/></svg><span style="margin-left:29px">Child 7</span></div>
      <div class="tree-child" style="left:48px;top:352px"><svg style="left:0;top:5px" width="6" height="12" viewBox="0 0 6 12"><path d="M1 1l4 5-4 5" fill="none" stroke="#bbb" stroke-width="1.5"/></svg><svg style="left:12px;top:3px" width="13" height="13" viewBox="0 0 24 24"><path d="M12 2l3 7 7 .6-5.4 4.7 1.7 7.2L12 17.6 5.7 21.5l1.7-7.2L2 9.6 9 9z" fill="var(--orange)"/></svg><span style="margin-left:29px">Child 8</span></div>
      <div class="tree-child" style="left:48px;top:377px"><svg style="left:0;top:5px" width="6" height="12" viewBox="0 0 6 12"><path d="M1 1l4 5-4 5" fill="none" stroke="#bbb" stroke-width="1.5"/></svg><svg style="left:12px;top:3px" width="13" height="13" viewBox="0 0 24 24"><path d="M12 2l3 7 7 .6-5.4 4.7 1.7 7.2L12 17.6 5.7 21.5l1.7-7.2L2 9.6 9 9z" fill="var(--orange)"/></svg><span style="margin-left:29px">Child 9</span></div>
      <div class="tree-child" style="left:48px;top:402px"><svg style="left:0;top:5px" width="6" height="12" viewBox="0 0 6 12"><path d="M1 1l4 5-4 5" fill="none" stroke="#bbb" stroke-width="1.5"/></svg><svg style="left:12px;top:3px" width="13" height="13" viewBox="0 0 24 24"><path d="M12 2l3 7 7 .6-5.4 4.7 1.7 7.2L12 17.6 5.7 21.5l1.7-7.2L2 9.6 9 9z" fill="var(--orange)"/></svg><span style="margin-left:29px">Child 10</span></div>
    </section>
  </main>

  <footer class="site-footer">
    <span class="social" style="left:89px;background:#3b5a99"></span>
    <span class="social" style="left:121px;background:#4fbde9"></span>
    <span class="social" style="left:153px;background:#1a79a8"></span>
    <div class="copyright">© 2013 Company Name.&nbsp; All right reserved</div>
  </footer>

</div>
</body>
</html>
```